Mira Solt makeup artist business cards

Hello
I need business cards for my freelance makeup artist business.

What I am looking for;
Sleek
Clear and easily read
Expensive/exclusive feel
Black and white
Embossed

Information that must be included on back
My name
My contact number
My email
My website
My Facebook
My Instagram

If it works I'd like to also include on the back;
Bridal, glamour, evening, editorial, fashion, tv, film makeup
(Open to exclude if it makes the card look to busy)

Industry/Entity Type

Business

Requirements
Must have
• My logo mira Solt makeup artist as shown in photos
Nice to have
• I'd like to see some designs with the social media icons (as shown in image attached)

```html
<!DOCTYPE html>
<html lang="en">
<head>
<meta charset="utf-8">
<title>Mira Solt – Makeup Artist Business Card</title>
<link rel="stylesheet" href="https://fonts.googleapis.com/css2?family=Josefin+Sans:wght@300;400&family=Montserrat:wght@500&display=swap">
<style>
  :root {
    --page-bg: #f5f5f5;
    --card-bg: #000000;
    --ink: #ffffff;
    --ink-soft: #d9d9d9;
    --dot: #f2f2f2;
    --wave-light: #8a8a8a;
    --wave-dark: #3a3a3a;
  }
  * { margin: 0; padding: 0; box-sizing: border-box; }
  html, body {
    width: 1200px;
    height: 967px;
    overflow: hidden;
    background: var(--page-bg);
  }
  .canvas {
    position: relative;
    width: 1200px;
    height: 967px;
  }
  .card {
    position: absolute;
    left: 299px;
    top: 313px;
    width: 590px;
    height: 356px;
    background: var(--card-bg);
    color: var(--ink);
  }
  .brand {
    position: absolute;
    left: 53px;
    top: 27px;
  }
  .brand-name {
    font-family: "Josefin Sans", sans-serif;
    font-weight: 300;
    font-size: 18px;
    letter-spacing: 4px;
    line-height: 1;
  }
  .brand-role {
    margin-top: 4px;
    font-family: "Josefin Sans", sans-serif;
    font-weight: 300;
    font-size: 7px;
    letter-spacing: 5.4px;
    color: var(--ink-soft);
  }
  .contact-list {
    position: absolute;
    left: 52px;
    top: 103px;
    list-style: none;
  }
  .contact-item {
    display: flex;
    align-items: center;
    height: 35px;
    font-family: "Montserrat", sans-serif;
    font-weight: 500;
    font-size: 11px;
    letter-spacing: 3.2px;
  }
  .contact-dot {
    width: 16px;
    height: 16px;
    border-radius: 50%;
    background: var(--dot);
    margin-right: 14px;
    flex: none;
  }
  .wave-pattern {
    position: absolute;
    right: 6px;
    top: 0;
    width: 90px;
    height: 356px;
    background: linear-gradient(90deg, var(--wave-dark), var(--wave-light) 45%, var(--wave-dark));
    opacity: 0.55;
  }
</style>
</head>
<body>
  <main class="canvas">
    <section class="card">
      <header class="brand">
        <h1 class="brand-name">MIRA SOLT</h1>
        <p class="brand-role">MAKEUP ARTIST</p>
      </header>
      <ul class="contact-list">
        <li class="contact-item"><span class="contact-dot"></span>999-99-99</li>
        <li class="contact-item"><span class="contact-dot"></span>EMAIADDRESS@COM.</li>
        <li class="contact-item"><span class="contact-dot"></span>YOURWEBSITE.COM</li>
        <li class="contact-item"><span class="contact-dot"></span>YOURFACEBOOK.COM</li>
        <li class="contact-item"><span class="contact-dot"></span>YOURINSTAGRAM.COM</li>
      </ul>
      <div class="wave-pattern" role="img" aria-label="Decorative pattern of flowing grey vertical wavy lines"></div>
    </section>
  </main>
</body>
</html>
```